Binder design for a veterinary clinic

We are seeking a talented designer to create a standout design for ring binders specifically for our veterinary clinic. These binders will be used to organize materials from our Continuing Professional Development (CPD) projects for colleagues and interns. The design should be clean, professional, and align with our brand guidelines. To give you a better understanding of our branding, we’ve included the design of our vehicles as a reference. As additional reference, please visit www.tierpraxoland.at

Target Market(s)

veterinarians

Industry/Entity Type

Veterinary

Font styles to use
Sans Serif

Colors
0054AA
0677BA
7BADD7
CADEEF
E8F1F8
FFC000
F8CF3A
FAE287
FDF2CF
FEFAEE

Requirements
Must have
• Our Logo an a clean design
Should not have
• to much images

```html
<!DOCTYPE html>
<html lang="de">
<head>
<meta charset="utf-8">
<title>Tierpraxoland – Ordner-Umschlag</title>
<link rel="stylesheet" href="https://fonts.googleapis.com/css2?family=Rubik:wght@400;500;700&family=Montserrat:wght@600&display=swap">
<style>
  :root {
    --paper: #e8dfcb;
    --navy: #24374b;
    --gold: #c99a2e;
    --white: #ffffff;
    --photo-light: #b9b9b9;
    --photo-dark: #6f6f6f;
    --cut: #d0312d;
    --text-font: "Rubik", Arial, sans-serif;
    --tag-font: "Montserrat", Arial, sans-serif;
  }
  * { margin: 0; padding: 0; box-sizing: border-box; }
  html, body { width: 1200px; height: 637px; overflow: hidden; background: var(--paper); }
  .binder { position: relative; width: 1200px; height: 637px; font-family: var(--text-font); }
  .shapes { position: absolute; inset: 0; }
  .brand-name {
    position: absolute; color: var(--white); font-weight: 700; line-height: 1;
    font-family: var(--text-font); text-align: center; letter-spacing: -0.5px; white-space: nowrap;
  }
  .tagline {
    position: absolute; color: var(--gold); font-family: var(--tag-font); line-height: 1;
    font-weight: 600; text-align: center; white-space: nowrap;
  }
  .back-name { left: 160px; width: 240px; top: 193px; font-size: 24px; }
  .back-intro {
    position: absolute; left: 55px; width: 462px; top: 238px;
    color: var(--white); font-size: 13.4px; line-height: 18.8px; text-align: center;
  }
  .spine-title {
    position: absolute; left: 601px; top: 272px; transform: translate(-50%, -50%) rotate(-90deg);
    display: flex; flex-direction: column; align-items: flex-start;
  }
  .spine-title .brand-name, .spine-title .tagline { position: static; }
  .spine-title .brand-name { font-size: 22px; line-height: 24px; }
  .spine-title .tagline { font-size: 9.5px; line-height: 12px; }
  .front-name { left: 763px; width: 300px; top: 192px; font-size: 31px; }
  .front-tag { left: 763px; width: 300px; top: 224px; font-size: 13px; }
  .contact { position: absolute; left: 670px; top: 508px; list-style: none; color: var(--navy); }
  .contact li { display: flex; align-items: flex-start; gap: 7px; font-size: 13.5px; font-weight: 500; line-height: 15.5px; margin-bottom: 14px; }
  .contact li:last-child { margin-bottom: 0; }
  .contact svg { flex: none; width: 21px; height: 21px; margin-top: -3px; }
</style>
</head>
<body>
<div class="binder">
  <svg class="shapes" width="1200" height="637" viewBox="0 0 1200 637">
    <defs>
      <linearGradient id="building-tone" x1="0" y1="0" x2="1" y2="1">
        <stop offset="0" stop-color="#b9b9b9"/>
        <stop offset="1" stop-color="#6f6f6f"/>
      </linearGradient>
    </defs>

    <!-- back cover -->
    <rect class="back-panel" x="27" y="27.5" width="513" height="581.5" fill="var(--navy)"/>
    <polygon class="corner-stripe" points="151,27.5 197,27.5 27,103 27,101" fill="var(--white)"/>
    <polygon class="corner-gold" points="27,27.5 151,27.5 27,101" fill="var(--gold)"/>
    <circle class="brand-dot" cx="280" cy="151" r="33" fill="var(--white)" stroke="var(--gold)" stroke-width="3"/>
    <g class="divider" fill="var(--gold)">
      <rect x="185" y="372" width="87" height="1.6"/>
      <rect x="297" y="372" width="86" height="1.6"/>
      <circle cx="285" cy="373" r="6"/>
    </g>
    <rect class="dog-silhouette" role="img" aria-label="Weiße Hundesilhouette im Profil" x="27" y="455" width="135" height="154" rx="40" fill="var(--white)"/>
    <polygon class="corner-stripe" points="540,489 540,494 349,609 285,609" fill="var(--white)"/>
    <polygon class="corner-gold" points="540,495 540,609 350,609" fill="var(--gold)"/>
    <rect class="cat-silhouette" role="img" aria-label="Dunkle Katzensilhouette auf Gold" x="455" y="533" width="60" height="76" rx="20" fill="var(--navy)"/>

    <!-- spine -->
    <rect class="hinge" x="540" y="27.5" width="16" height="581.5" fill="var(--paper)"/>
    <rect class="hinge" x="643" y="27.5" width="15" height="581.5" fill="var(--paper)"/>
    <line x1="548" y1="28" x2="548" y2="609" stroke="var(--cut)" stroke-width="0.6" stroke-dasharray="3 2"/>
    <line x1="651" y1="28" x2="651" y2="609" stroke="var(--cut)" stroke-width="0.6" stroke-dasharray="3 2"/>
    <rect class="spine-panel" x="556" y="27.5" width="87" height="581.5" fill="var(--navy)"/>
    <circle class="brand-dot" cx="601" cy="396" r="36" fill="var(--white)" stroke="var(--gold)" stroke-width="3"/>

    <!-- front cover -->
    <rect class="front-panel" x="658" y="27.5" width="514" height="581.5" fill="var(--navy)"/>
    <polygon class="corner-stripe" points="964,27.5 1002,27.5 1172,114 1172,119" fill="var(--white)"/>
    <polygon class="corner-gold" points="1020,27.5 1172,27.5 1172,111" fill="var(--gold)"/>
    <circle class="brand-dot" cx="913" cy="132" r="50" fill="var(--white)" stroke="var(--gold)" stroke-width="4"/>
    <polygon class="clinic-photo" role="img" aria-label="Foto des Klinikgebäudes mit Dachpergola und Schriftzug an der Fassade" points="658,405 830,345 1065,285 1172,355 1172,609 658,609" fill="url(#building-tone)"/>
    <polygon class="corner-stripe" points="658,404 1093,609 658,609" fill="var(--white)"/>
    <polygon class="corner-band" points="658,408 1048,609 658,609" fill="var(--navy)"/>
    <polygon class="corner-gold" points="658,412 995,609 658,609" fill="var(--gold)"/>
  </svg>

  <div class="brand-name back-name">Tierpraxoland</div>
  <p class="back-intro">Das Tierpraxoland ist eine der größten und modernsten privaten Tierkliniken Europas direkt im Süden Wiens. Bei uns hat die beste tiermedizinische Versorgung Ihres Vierbeiners oberste Priorität. Neben der herausragenden fachlichen Expertise unserer Spezialisten bieten wir topmoderne diagnostische und therapeutische Möglichkeiten. Für Notfälle ist das Tierpraxoland rund-um-die-Uhr besetzt.</p>

  <div class="spine-title">
    <div class="brand-name">Tierpraxoland</div>
    <div class="tagline">Fachklinik für Kleintiere</div>
  </div>

  <div class="brand-name front-name">Tierpraxoland</div>
  <div class="tagline front-tag">Fachklinik für Kleintiere</div>

  <ul class="contact">
    <li>
      <svg viewBox="0 0 20 20"><circle cx="10" cy="10" r="10" fill="var(--navy)"/><path d="M7 5.2l1.6 2.6-1 1.1c.6 1.3 1.5 2.2 2.7 2.8l1.1-1 2.5 1.6-.6 1.8c-3.9-.3-7-3.4-7.3-7.3z" fill="var(--white)"/></svg>
      <span>+43(0)1 55 01928</span>
    </li>
    <li>
      <svg viewBox="0 0 20 20"><circle cx="10" cy="10" r="10" fill="var(--navy)"/><rect x="5" y="6.5" width="10" height="7" fill="none" stroke="var(--white)" stroke-width="1.2"/><path d="M5 6.5l5 4 5-4" fill="none" stroke="var(--white)" stroke-width="1.2"/></svg>
      <span>info@tierpraxoland.at</span>
    </li>
    <li>
      <svg viewBox="0 0 20 20"><circle cx="10" cy="10" r="10" fill="var(--navy)"/><path d="M10 4.5a3.6 3.6 0 0 1 3.6 3.6c0 2.6-3.6 7-3.6 7s-3.6-4.4-3.6-7A3.6 3.6 0 0 1 10 4.5z" fill="var(--white)"/><circle cx="10" cy="8.2" r="1.3" fill="var(--navy)"/></svg>
      <span>Tierpraxoland GmbH &amp; Co KG<br>Lindenhofgasse 18 1230 Vienna</span>
    </li>
  </ul>
</div>
</body>
</html>
```